Meridian Swift add on sales tool2017

This will be a flyer to leave with our clients we just did work for. We want to entice them to use our other services over the next 30 days with a discount, money off etc. we will write in the special and the expiration date. I want the client to read the description and see a picture of the service they may want done.

Target Market(s)

Repeat clients

Industry/Entity Type

Cleaning Service

Font styles to use
Serif
Sans Serif

Colors
ec1f27
000000
b1b1b1

Requirements
Must have
• Call to action! look high end market, clients show we do 1st class work.
• Don't Waite
Nice to have
• Classy, quality, I'm open to using other pictures that may look better
Should not have
• Look like a typical carpet cleaners special flyer
• Not to look cluttered

```html
<!DOCTYPE html>
<html lang="en">
<head>
<meta charset="utf-8">
<title>Meridian Swift – 30 Day Special Offer</title>
<link href="https://fonts.googleapis.com/css2?family=Open+Sans:wght@300;400;600;700;800&family=Roboto+Condensed:wght@700&display=swap" rel="stylesheet">
<style>
  :root {
    --red: #ec1f27;
    --black: #000000;
    --ink: #222222;
    --band: #2b2b2b;
    --grey: #b1b1b1;
    --panel: #e9eaea;
    --divider: #d6d6d6;
    --footer: #555555;
    --white: #ffffff;
  }
  * { box-sizing: border-box; margin: 0; padding: 0; }
  html, body { width: 1041px; height: 1200px; overflow: hidden; background: var(--white); }
  body { font-family: "Open Sans", Arial, sans-serif; color: var(--ink); }

  .flyer { position: relative; width: 1041px; height: 1200px; background: var(--white); }

  /* Header */
  .header { position: absolute; top: 0; left: 0; width: 1041px; height: 194px; display: flex; }
  .brand { width: 387px; height: 194px; background: var(--white); display: flex; align-items: center; justify-content: center; gap: 12px; }
  .brand-dot { width: 34px; height: 34px; border-radius: 50%; background: var(--red); }
  .brand-name { font-weight: 700; font-size: 30px; color: var(--red); letter-spacing: 0.5px; }
  .offer { position: relative; flex: 1; background: var(--panel); }
  .offer-red { position: absolute; top: 0; height: 58px; background: var(--red); }
  .offer-red.left { left: 0; width: 80px; }
  .offer-red.right { right: 0; width: 78px; }
  .offer-banner { position: absolute; top: 0; left: 84px; right: 84px; height: 58px; background: linear-gradient(#1c1c1c, #3a3a3a); display: flex; align-items: center; justify-content: center; font-family: "Roboto Condensed", "Arial Narrow", sans-serif; font-size: 36px; color: var(--white); letter-spacing: 0.5px; }
  .offer-banner .hot { color: var(--red); margin-left: 10px; }
  .expires { position: absolute; left: 16px; top: 156px; font-weight: 600; font-size: 21px; color: var(--ink); }

  /* Title band */
  .title { position: absolute; top: 201px; left: 0; width: 1041px; height: 107px; background: var(--band); text-align: center; color: var(--white); }
  .title-top { font-weight: 300; font-size: 45px; line-height: 48px; padding-top: 6px; letter-spacing: 0.5px; }
  .title-main { font-weight: 700; font-size: 52px; line-height: 52px; letter-spacing: 1px; }
  .title-main .hot { color: var(--red); }

  /* Services */
  .services { position: absolute; top: 313px; left: 0; width: 1041px; }
  .service { position: relative; height: 157px; margin-bottom: 8px; display: flex; background: var(--white); }
  .service::after { content: ""; position: absolute; left: 0; right: 0; bottom: -8px; height: 8px; background: var(--divider); }
  .service-photo { width: 325px; height: 157px; clip-path: polygon(0 0, 91% 0, 100% 50%, 91% 100%, 0 100%); position: relative; }
  .step { position: absolute; top: 4px; left: 3px; font-weight: 700; font-size: 11px; color: var(--black); line-height: 11px; text-align: center; }
  .step-num { display: block; width: 16px; height: 16px; margin: 2px 0 0 2px; border-radius: 50%; background: var(--red); color: var(--white); font-size: 11px; line-height: 16px; }
  .service-text { flex: 1; padding: 18px 36px 0 30px; }
  .service-title { display: inline-block; font-weight: 800; font-size: 27px; line-height: 32px; color: var(--ink); padding-right: 8px; border-bottom: 3px solid var(--ink); box-shadow: 0 3px 0 -0px transparent; }
  .service-title .hot { color: var(--red); }
  .service-body { margin-top: 14px; font-size: 18.5px; line-height: 28px; color: var(--ink); }

  .photo-carpet { background: linear-gradient(135deg, #cfc6b5 0%, #9b9488 45%, #6b5a45 100%); }
  .photo-upholstery { background: linear-gradient(90deg, #7b7f6c 0%, #a7a88f 48%, #c9c6ad 52%, #8a5048 100%); }
  .photo-drapery { background: linear-gradient(90deg, #6d5a4e 0%, #2a2624 45%, #c8cbcf 75%, #7e6a5c 100%); }
  .photo-tile { background: linear-gradient(135deg, #6f6d6c 0%, #a39c92 50%, #7b7673 100%); }
  .photo-stone { background: linear-gradient(160deg, #9a9c94 0%, #d8d9d2 40%, #5f625c 100%); }

  /* Footer */
  .footer { position: absolute; left: 0; bottom: 0; width: 1041px; height: 66px; background: var(--footer); }
  .cta { position: absolute; left: 24px; top: 0; height: 66px; line-height: 66px; font-family: "Roboto Condensed", "Arial Narrow", sans-serif; font-size: 36px; color: var(--white); }
  .phone-box { position: absolute; left: 386px; top: 0; width: 328px; height: 66px; }
  .phone-box svg { position: absolute; inset: 0; }
  .phone-number { position: absolute; inset: 0; text-align: center; line-height: 66px; font-family: "Roboto Condensed", "Arial Narrow", sans-serif; font-size: 44px; color: var(--white); }
  .address { position: absolute; left: 732px; top: 10px; font-weight: 700; font-size: 17px; line-height: 23px; color: var(--white); }
  .address-line { display: flex; align-items: center; gap: 6px; }
  .address-line.indent { padding-left: 22px; }
</style>
</head>
<body>
<div class="flyer">
  <header class="header">
    <div class="brand">
      <span class="brand-dot"></span>
      <span class="brand-name">MERIDIAN SWIFT</span>
    </div>
    <div class="offer">
      <span class="offer-red left"></span>
      <div class="offer-banner">30 DAY <span class="hot">SPECIAL OFFER!</span></div>
      <span class="offer-red right"></span>
      <div class="expires">Expires</div>
    </div>
  </header>

  <section class="title">
    <div class="title-top">ONE STOP FOR ALL YOUR</div>
    <div class="title-main">HOME <span class="hot">CLEANING</span> NEEDS</div>
  </section>

  <section class="services">
    <article class="service">
      <div class="service-photo photo-carpet" role="img" aria-label="Photo of freshly cleaned carpeted staircase">
        <div class="step">STEP<span class="step-num">1</span></div>
      </div>
      <div class="service-text">
        <h2 class="service-title"><span class="hot">CARPET</span> CLEANING</h2>
        <p class="service-body">Don't let dirty carpets spoil the look of your beautiful home!. with 37 years of cleaning carpets experience you can expect your carpets to look like new in most&nbsp; cases.</p>
      </div>
    </article>

    <article class="service">
      <div class="service-photo photo-upholstery" role="img" aria-label="Before and after photo of a cleaned upholstered sofa">
        <div class="step">STEP<span class="step-num">2</span></div>
      </div>
      <div class="service-text">
        <h2 class="service-title"><span class="hot">UPHOLSTERY</span> CLEANING</h2>
        <p class="service-body">Every day use leaves your sofa's and chairslookng dingy and can smell like dog. Our Dry cleaning ,Shampoo or Rinse extraxtionwill leave the fabric feel like clean sheet!</p>
      </div>
    </article>

    <article class="service">
      <div class="service-photo photo-drapery" role="img" aria-label="Technician dry cleaning draperies in a home">
        <div class="step">STEP<span class="step-num">3</span></div>
      </div>
      <div class="service-text">
        <h2 class="service-title"><span class="hot">DRAPERY</span> CLEANING</h2>
        <p class="service-body">Drapery's act like a filter atracting atmisphiric soil!Making them look dingy, We make it easy to Dry clean in-home! Safe and efective beautifuldrapery again.</p>
      </div>
    </article>

    <article class="service">
      <div class="service-photo photo-tile" role="img" aria-label="Close-up of tile floor with cleaned and uncleaned grout">
        <div class="step">STEP<span class="step-num">4</span></div>
      </div>
      <div class="service-text">
        <h2 class="service-title"><span class="hot">TILE &amp; GROUT</span> CLEANING</h2>
        <p class="service-body">Tile &amp; Grout get neglected! Dirty grout can leave permanent staining. Let our professionals bring back the look of a new floor.</p>
      </div>
    </article>

    <article class="service">
      <div class="service-photo photo-stone" role="img" aria-label="Polished marble floor reflecting window light">
        <div class="step">STEP<span class="step-num">5</span></div>
      </div>
      <div class="service-text" style="padding-top:10px">
        <h2 class="service-title" style="border-bottom:none;padding:0"><span class="hot">NATURAL STONE</span></h2><br>
        <h2 class="service-title">CLEANING &amp; POLISHING</h2>
        <p class="service-body" style="margin-top:10px">A dull stained Marble - Granite-Travertine and other Natural stone can be revitalized to look NEW again!</p>
      </div>
    </article>
  </section>

  <footer class="footer">
    <div class="cta">CALL NOW TO BOOK</div>
    <div class="phone-box">
      <svg width="328" height="66" viewBox="0 0 328 66" aria-hidden="true">
        <polygon points="0,0 306,0 322,33 306,66 0,66 14,33" fill="#ffffff"/>
        <polygon points="4,0 300,0 316,33 300,66 4,66 18,33" fill="#ec1f27"/>
      </svg>
      <div class="phone-number">702 555-0147</div>
    </div>
    <div class="address">
      <div class="address-line">
        <svg width="16" height="20" viewBox="0 0 16 20" aria-hidden="true"><path d="M8 0C3.6 0 0 3.5 0 7.8 0 13.5 8 20 8 20s8-6.5 8-12.2C16 3.5 12.4 0 8 0zm0 11a3.2 3.2 0 1 1 0-6.4A3.2 3.2 0 0 1 8 11z" fill="#ffffff"/></svg>
        <span>4180 Canyon Ridge Rd. Suite B</span>
      </div>
      <div class="address-line indent">702 555-0147 Las Vegas</div>
    </div>
  </footer>
</div>
</body>
</html>
```